IT Consulting company Needs a Logo Design and Business Cards

I need a New Logo and Business Cards for an established IT Managed Services Company that specializes in flat-rate managed IT services. We provide Design and Build, Help Desk, Onsite and Remote Support Services.

Target Market(s)

Corporate Clients

Industry/Entity Type

It Company

Logo Text

Halbrook Computer Group

Requirements
Nice to have
• Tag Line= Technology at Lightning Speed

```html
<!DOCTYPE html>
<html lang="en">
<head>
<meta charset="utf-8">
<title>Halbrook Computer Group – Business Cards</title>
<link rel="stylesheet" href="https://fonts.googleapis.com/css2?family=Questrial&display=swap">
<style>
  :root {
    --backdrop: #3c4144;
    --card: #ffffff;
    --brand-blue: #0f75b4;
    --brand-sky: #c6e6f8;
    --shadow: rgba(0, 0, 0, 0.45);
  }
  html, body {
    margin: 0;
    padding: 0;
    width: 1200px;
    height: 1000px;
    overflow: hidden;
    background: var(--backdrop);
    font-family: "Questrial", "Century Gothic", sans-serif;
  }
  .canvas {
    position: relative;
    width: 1200px;
    height: 1000px;
  }
  .card {
    position: absolute;
    background: var(--card);
    box-shadow: 0 8px 22px var(--shadow);
  }
  .card--front {
    left: 118px;
    top: 84px;
    width: 712px;
    height: 394px;
  }
  .card--back {
    left: 380px;
    top: 518px;
    width: 726px;
    height: 417px;
  }
  .brand-mark {
    position: absolute;
    background: var(--brand-sky);
  }
  .card--front .brand-mark {
    left: 140px;
    top: 158px;
    width: 92px;
    height: 86px;
  }
  .card--back .brand-mark {
    left: 120px;
    top: 148px;
    width: 118px;
    height: 110px;
  }
  .brand-lockup {
    position: absolute;
    left: 277px;
    top: 152px;
    color: var(--brand-blue);
    font-weight: 400;
  }
  .brand-name {
    margin: 0;
    line-height: 1;
    font-weight: 400;
    color: var(--brand-blue);
    text-transform: uppercase;
  }
  .brand-name__primary {
    display: block;
    font-size: 49px;
    letter-spacing: 3px;
  }
  .brand-name__secondary {
    display: block;
    margin-top: 4px;
    font-size: 26px;
    letter-spacing: 0.5px;
  }
  .tagline {
    margin: 6px 0 0;
    font-size: 17px;
    letter-spacing: 0.6px;
    color: var(--brand-blue);
  }
  .holder-name {
    position: absolute;
    left: 398px;
    top: 68px;
    margin: 0;
    font-size: 20px;
    font-weight: 400;
    letter-spacing: 5px;
    color: var(--brand-blue);
  }
  .contact-list {
    position: absolute;
    left: 393px;
    top: 240px;
    margin: 0;
    padding: 0;
    list-style: none;
  }
  .contact-item {
    display: flex;
    align-items: center;
    height: 38px;
    font-size: 23px;
    color: var(--brand-blue);
  }
  .contact-item svg {
    width: 22px;
    height: 22px;
    margin-right: 10px;
    fill: var(--brand-blue);
  }
</style>
</head>
<body>
<main class="canvas">
  <section class="card card--front" aria-label="Business card front">
    <div class="brand-mark" aria-hidden="true"></div>
    <div class="brand-lockup">
      <h1 class="brand-name">
        <span class="brand-name__primary">Halbrook</span>
        <span class="brand-name__secondary">Computer Group</span>
      </h1>
      <p class="tagline">Technology at Lightning Speed</p>
    </div>
  </section>

  <section class="card card--back" aria-label="Business card back">
    <div class="brand-mark" aria-hidden="true"></div>
    <h2 class="holder-name">NAME</h2>
    <ul class="contact-list">
      <li class="contact-item">
        <svg viewBox="0 0 24 24" aria-hidden="true"><path d="M6.6 10.8c1.4 2.8 3.8 5.1 6.6 6.6l2.2-2.2c.3-.3.7-.4 1-.2 1.1.4 2.3.6 3.6.6.6 0 1 .4 1 1V20c0 .6-.4 1-1 1C10.6 21 3 13.4 3 4c0-.6.4-1 1-1h3.5c.6 0 1 .4 1 1 0 1.3.2 2.5.6 3.6.1.3 0 .7-.2 1l-2.3 2.2z"/></svg>
        000 000
      </li>
      <li class="contact-item">
        <svg viewBox="0 0 24 24" aria-hidden="true"><path d="M2 5h20v14H2z M3.5 6.5 12 12.5l8.5-6z" fill-rule="evenodd"/></svg>
        ......halbrookcg.com
      </li>
      <li class="contact-item">
        <svg viewBox="0 0 24 24" aria-hidden="true" fill="none" stroke="#0f75b4" stroke-width="1.8"><circle cx="12" cy="12" r="9.5"/><ellipse cx="12" cy="12" rx="4" ry="9.5"/><path d="M2.5 12h19M4 7h16M4 17h16"/></svg>
        www.halbrookcg.com
      </li>
    </ul>
  </section>
</main>
</body>
</html>
```